FOLI PACK FOR STICKS

Design the packaging for salted sticks (weight 400g) reference to the logo TOVEN (in attached).
Color packaging- look forward to suggestions.
Package with window.
Hi, we need only graphic conception without texts on back side.

Please find Logo TOVEN and the grid of packaging - attached
Updates

we need only graphic conception without texts on back side. Added Saturday, November 08, 2014

Target Market(s)

typical salted snack for everyone (adults and children included)

Font styles to use
Sans Serif

Requirements
Should not have
• - religion and politic signs…
• - toys and childdraws
• - monsters, devils and demons etc.

```html
<!DOCTYPE html>
<html lang="en">
<head>
<meta charset="utf-8">
<title>TOVEN Salted Sticks – Front Pack</title>
<link rel="stylesheet" href="https://fonts.googleapis.com/css2?family=Baloo+2:wght@800&family=Roboto:wght@700&display=swap">
<style>
  :root {
    --backdrop: #ececec;
    --foil-red: #e01f26;
    --foil-red-deep: #b8121a;
    --foil-red-light: #f2464c;
    --stripe-white: #ffffff;
    --stripe-pink: #f3868c;
    --window-amber: #d98a2a;
    --window-gold: #f0b04a;
    --window-brown: #9c5418;
    --label-white: #ffffff;
    --brand-brown: #6e4217;
    --headline-white: #ffffff;
    --headline-shadow: #a50f16;
    --weight-grey: #b9b9b9;
  }
  html, body {
    margin: 0;
    padding: 0;
    width: 900px;
    height: 1200px;
    overflow: hidden;
    background: var(--backdrop);
  }
  .canvas {
    position: relative;
    width: 900px;
    height: 1200px;
  }
  .pack-art {
    position: absolute;
    inset: 0;
  }
  .brand-name {
    position: absolute;
    left: 255px;
    top: 455px;
    width: 370px;
    margin: 0;
    text-align: center;
    font-family: "Roboto", Arial, sans-serif;
    font-weight: 700;
    font-size: 80px;
    letter-spacing: 1px;
    line-height: 1;
    color: var(--brand-brown);
  }
  .product-name {
    position: absolute;
    left: 150px;
    top: 640px;
    width: 590px;
    margin: 0;
    text-align: center;
    font-family: "Baloo 2", "Arial Rounded MT Bold", Arial, sans-serif;
    font-weight: 800;
    font-size: 112px;
    line-height: 100px;
    letter-spacing: -1px;
    color: var(--headline-white);
    text-shadow: 4px 5px 0 var(--headline-shadow);
  }
  .product-name span { display: block; }
  .net-weight {
    position: absolute;
    left: 150px;
    top: 952px;
    width: 590px;
    margin: 0;
    text-align: center;
    font-family: "Roboto", Arial, sans-serif;
    font-weight: 700;
    font-size: 30px;
    color: var(--weight-grey);
  }
</style>
</head>
<body>
<main class="canvas">
  <svg class="pack-art" width="900" height="1200" viewBox="0 0 900 1200" xmlns="http://www.w3.org/2000/svg">
    <defs>
      <linearGradient id="foil-sheen" x1="0" y1="0" x2="0" y2="1">
        <stop offset="0" stop-color="var(--foil-red)"/>
        <stop offset="0.55" stop-color="var(--foil-red)"/>
        <stop offset="0.78" stop-color="var(--foil-red-deep)"/>
        <stop offset="0.9" stop-color="var(--foil-red-light)"/>
        <stop offset="1" stop-color="var(--foil-red)"/>
      </linearGradient>
      <linearGradient id="sticks-tone" x1="0" y1="0" x2="1" y2="0">
        <stop offset="0" stop-color="var(--window-amber)"/>
        <stop offset="0.3" stop-color="var(--window-gold)"/>
        <stop offset="0.6" stop-color="var(--window-brown)"/>
        <stop offset="1" stop-color="var(--window-amber)"/>
      </linearGradient>
    </defs>

    <rect class="pouch-body" x="150" y="160" width="590" height="895" fill="url(#foil-sheen)"/>

    <path class="product-window" role="img" aria-label="Photo of golden salted sticks lying side by side"
      fill="url(#sticks-tone)"
      d="M150 238 q18.5 -8 37 0 t37 0 t37 0 t37 0 t37 0 t37 0 t37 0 t37 0 t37 0 t37 0 t37 0 t37 0 t37 0 t37 0 t37 0 t35 0
         L740 580 q-18.5 8 -37 0 t-37 0 t-37 0 t-37 0 t-37 0 t-37 0 t-37 0 t-37 0 t-37 0 t-37 0 t-37 0 t-37 0 t-37 0 t-37 0 t-37 0 t-35 0 Z"/>

    <path class="stripe-top" fill="none" stroke="var(--stripe-white)" stroke-width="5"
      d="M150 236 q18.5 -8 37 0 t37 0 t37 0 t37 0 t37 0 t37 0 t37 0 t37 0 t37 0 t37 0 t37 0 t37 0 t37 0 t37 0 t37 0 t35 0"/>
    <path class="stripe-white" fill="none" stroke="var(--stripe-white)" stroke-width="6"
      d="M150 588 q18.5 -8 37 0 t37 0 t37 0 t37 0 t37 0 t37 0 t37 0 t37 0 t37 0 t37 0 t37 0 t37 0 t37 0 t37 0 t37 0 t35 0"/>
    <path class="stripe-pink" fill="none" stroke="var(--stripe-pink)" stroke-width="7"
      d="M150 605 q18.5 -8 37 0 t37 0 t37 0 t37 0 t37 0 t37 0 t37 0 t37 0 t37 0 t37 0 t37 0 t37 0 t37 0 t37 0 t37 0 t35 0"/>
    <path class="stripe-thin" fill="none" stroke="var(--stripe-pink)" stroke-width="3" opacity="0.7"
      d="M150 620 q18.5 -8 37 0 t37 0 t37 0 t37 0 t37 0 t37 0 t37 0 t37 0 t37 0 t37 0 t37 0 t37 0 t37 0 t37 0 t37 0 t35 0"/>

    <path class="brand-label" fill="var(--label-white)"
      d="M280 382 H335 Q338 340 380 336 H500 Q540 340 545 382 H600 Q625 382 625 407 V572 Q625 597 600 597 H280 Q255 597 255 572 V407 Q255 382 280 382 Z"/>
  </svg>

  <p class="brand-name">TOVEN</p>

  <h1 class="product-name"><span>Salted</span><span>Sticks</span></h1>

  <p class="net-weight">400g</p>
</main>
</body>
</html>
```